Wordpress template re-design of current website

We need a WordPress template design and new look for our existing website. Our existing site it located at www.velmoro.com.au We are a tech company and want a fresh, clean modern website that matches our brand, services and logo colors. Our main Services are hospitality solutions, Velmoro TV solution and managed networks, more information on these can come from our existing website.

Target Market(s)

We are a tech company so must have a modern feel for new technology

Industry/Entity Type

It Company

Number of Pages Required

5+ page

Font styles to use
Sans Serif

Requirements
Must have
• Be based on a wordpress templete design and match the services that we have in our existing website, in the testimonials want a place for video testimonials as well as text. Nice clean icons used for graphics to represent services.
Nice to have
• nice visual representation of our services in the way of clean icons etc
Should not have
• Clutter

```html
<!DOCTYPE html>
<html lang="en">
<head>
<meta charset="utf-8">
<title>Velmoro — Wireless Internet</title>
<link rel="stylesheet" href="https://fonts.googleapis.com/css2?family=Source+Sans+3:wght@400;600&display=swap">
<style>
:root{
  --brand:#0b4a8f;
  --ink:#333b44;
  --white:#ffffff;
  --sky-top:#8d9bb0;
  --sky-mid:#a7b1c0;
  --water:#6e7c90;
  --shore:#2b3340;
}
*{margin:0;padding:0;box-sizing:border-box}
html,body{width:1200px;height:748px;overflow:hidden;background:var(--white)}
body{font-family:"Source Sans 3",sans-serif;position:relative}
.site-header{position:absolute;left:0;top:0;width:1200px;height:75px;background:var(--white)}
.brand{position:absolute;left:108px;top:14px;display:flex;align-items:center;gap:8px;color:var(--brand);font-size:30px;font-weight:600;line-height:1}
.brand-dot{width:12px;height:12px;border-radius:50%;background:var(--brand)}
.main-nav{position:absolute;top:0;height:75px}
.nav-item{position:absolute;top:34px;transform:translateX(-50%);font-size:15px;color:var(--ink);white-space:nowrap;text-decoration:none}
.nav-item.is-active{color:var(--brand)}
.nav-item.is-active::after{content:"";position:absolute;left:-9px;right:-9px;top:22px;height:2px;background:var(--brand)}
.hero{position:absolute;left:0;top:75px;width:1200px;height:673px;overflow:hidden}
.hero-photo{position:absolute;inset:0;background:
  linear-gradient(180deg,var(--sky-top) 0%,var(--sky-mid) 30%,#98a1b1 52%,#4f5868 60%,var(--water) 68%,#5d6a7d 88%,var(--shore) 100%)}
.hero-shade{position:absolute;inset:0;background:rgba(20,28,42,.28)}
.hero-copy{position:absolute;left:0;top:0;color:var(--white)}
.hero-title{position:absolute;left:109px;top:176px;font-size:56px;font-weight:400;white-space:nowrap;letter-spacing:.5px}
.hero-rule{position:absolute;left:112px;top:263px;width:159px;height:1px;background:var(--white)}
.hero-sub{position:absolute;left:109px;top:290px;font-size:41px;font-weight:400;line-height:54px;white-space:nowrap}
.btn{position:absolute;top:446px;width:125px;height:42px;display:flex;align-items:center;justify-content:center;font-size:13px;color:var(--white);text-decoration:none}
.btn-primary{left:112px;background:var(--brand)}
.btn-ghost{left:254px;border:1px solid var(--white)}
.slider-arrow{position:absolute;top:288px}
.slider-arrow.prev{left:30px}
.slider-arrow.next{left:1150px}
.slider-dots{position:absolute;top:604px;left:558px;display:flex;gap:15px}
.dot{width:18px;height:18px;border:1.5px solid var(--white)}
.dot.is-current{background:var(--white)}
</style>
</head>
<body>
<header class="site-header">
  <div class="brand"><span>Velmoro</span><span class="brand-dot"></span></div>
  <nav class="main-nav">
    <a class="nav-item is-active" style="left:475px">HOME</a>
    <a class="nav-item" style="left:590px">SERVICES</a>
    <a class="nav-item" style="left:706px">ABOUT</a>
    <a class="nav-item" style="left:821px">WORK</a>
    <a class="nav-item" style="left:937px">CONTACT US</a>
  </nav>
</header>
<section class="hero">
  <div class="hero-photo" role="img" aria-label="Photo of a person with a camera standing by a calm lake at dusk, hills and clouded sky behind"></div>
  <div class="hero-shade"></div>
  <div class="hero-copy">
    <h1 class="hero-title">Velmoro</h1>
    <div class="hero-rule"></div>
    <p class="hero-sub">Full Mobile<br>3G &amp; 4G Solutions</p>
    <a class="btn btn-primary">EXPLORE</a>
    <a class="btn btn-ghost">LEARN MORE</a>
  </div>
  <svg class="slider-arrow prev" width="20" height="30" viewBox="0 0 20 30" aria-label="Previous slide"><path d="M16 2 L3 15 L16 28" fill="none" stroke="#fff" stroke-width="1.5" opacity=".85"/></svg>
  <svg class="slider-arrow next" width="20" height="30" viewBox="0 0 20 30" aria-label="Next slide"><path d="M4 2 L17 15 L4 28" fill="none" stroke="#fff" stroke-width="1.5" opacity=".85"/></svg>
  <div class="slider-dots">
    <span class="dot is-current"></span><span class="dot"></span><span class="dot"></span>
  </div>
</section>
</body>
</html>
```